Lumo.app Homepage Redesign

We are seeking a talented designer to create an emotive and aspirational homepage for our website (www.lumo.app) that elevates the Lumo.app brand using our new home page copy.

Our current design feels product-heavy and lacks the global, professional, and emotive touch we're aiming for.

We want to strip back unnecessary visual distractions and focus on a more streamlined, compelling design that resonates with our audience.

Project Goals:
Replace product-heavy, literal imagery with more evocative, aspirational visuals.
Create a homepage that feels aspirational and professional, reflecting our global ambitions.
Explore the use of icons or simple graphics to reduce visual clutter and create a more refined experience.
Ensure that usability principles are at the forefront of the design. Navigation must be clear and accessible on both desktop and mobile.
Practicality is key. Any animations or transitions should serve a functional purpose and should not hinder website speed or performance.
We prefer mockups in Adobe XD for ease of use by our developer, but Photoshop is also acceptable if this suits your workflow better.

Design Considerations:
Imagery: The selected imagery should enhance the emotive feel of the site, not simply fill space.
Usability: Avoid hidden navigation on desktop, and ensure key call-to-action buttons like "Watch Demo" and "Book a Demo" are clearly identifiable as clickable.
Animations/Transitions: Any animated elements should focus on showcasing our content, not just adding visual flair. Consider website performance and practicality in your design.
Content Hierarchy: Follow the suggested hierarchy based on provided copy, giving prominence to our key propositions while minimizing distractions.
Style: Maintain Lumo.app's colour scheme and font set, but we welcome fresh perspectives on how to apply them.
Copy: We will be providing new written copy to replace the current content on the website. The new design should complement and elevate the revised messaging.

Deliverables:
An initial homepage mock-up based on our brand guidelines.
Two rounds of feedback and revisions based on our input.
Final design files provided in Adobe XD (preferred) or Photoshop.

Brand Resources:
You will be given access to our Adobe Library, Brand Guidelines, and new website copy (and indicative wireframe), along with any necessary imagery from our stock library.
Note: please contact us if you would like access to our Adobe Library.

Number of Pages Required

1 page

Font styles to use
Sans Serif
Other font styles liked:
• Poppins Bold, Proxima Nova Light, Bold.

Colors

Designer to choose colors to be used in the design.

Requirements
Must have
• New website copy as supplied and ideally follow the wireframe provided. Aspirational visuals. Meets our brand guidelines
Should not have
• Stock standard imagery.

```html
<!DOCTYPE html>
<html lang="en">
<head>
<meta charset="utf-8">
<title>Lumo.app — Connect the Unconnected</title>
<link href="https://fonts.googleapis.com/css2?family=Poppins:wght@600;700;800&family=Figtree:wght@300;400;500;600;700&display=swap" rel="stylesheet">
<style>
:root{
  --teal:#14b3b7;
  --teal-dark:#0b8f95;
  --red:#c8102e;
  --red-deep:#a00d22;
  --ink:#1b1b1b;
  --grey:#6b6b6b;
  --pale:#eef7f9;
  --white:#ffffff;
}
*{box-sizing:border-box;margin:0;padding:0}
html,body{width:1200px;height:4666px;overflow:hidden;background:var(--white)}
body{font-family:"Figtree",sans-serif;color:var(--ink);position:relative}
.abs{position:absolute}
.h-display{font-family:"Poppins",sans-serif;font-weight:800;text-transform:uppercase;letter-spacing:.2px}
.center{left:0;width:1200px;text-align:center}
.btn{position:absolute;display:flex;align-items:center;justify-content:center;border-radius:22px;color:var(--white);font-weight:700;font-size:15px;text-decoration:none}
.btn-teal{background:var(--teal)}
.btn-red{background:var(--red)}
.btn-white{background:var(--white);color:var(--red)}
.photo{position:absolute;border-radius:22px;box-shadow:0 8px 22px rgba(0,0,0,.18)}

/* hero */
.hero{position:absolute;left:0;top:0;width:1200px;height:600px;overflow:hidden}
.hero-photo{position:absolute;inset:0;background:linear-gradient(100deg,#0d1a26 0%,#1c2d3a 40%,#4a5058 62%,#8d8d8a 80%,#3d4044 100%)}
.logo-word{font-family:"Poppins",sans-serif;font-weight:800;font-size:38px;letter-spacing:-1px}
.nav{position:absolute;top:38px;left:385px;display:flex;gap:0;font-size:16px;color:var(--white)}
.nav a{color:var(--white);text-decoration:none;position:absolute;white-space:nowrap}
.nav a.active{color:var(--teal)}
.hero h1{position:absolute;left:110px;top:150px;color:var(--white);line-height:1.1}
.hero h1 .l1{display:block;font-size:60px}
.hero h1 .l2{display:block;font-size:41px;margin-top:6px}
.hero p{position:absolute;left:111px;top:278px;width:460px;color:var(--white);font-size:20px;line-height:36px}

/* section text */
.sec-title{position:absolute;font-family:"Poppins",sans-serif;font-weight:700;font-size:32px;text-transform:uppercase;color:var(--ink)}
.lead{position:absolute;font-size:18px;line-height:33px;color:var(--grey)}
.lead a{color:var(--teal);text-decoration:none;font-weight:600}
.lead-strong{position:absolute;font-size:18px;line-height:33px;color:var(--ink);font-weight:500}

/* services */
.svc{position:absolute;width:234px;height:92px;border-radius:14px;background:var(--white);box-shadow:0 4px 18px rgba(0,0,0,.1);display:flex;align-items:center;padding-left:20px;gap:20px;font-size:16px;font-weight:600;line-height:24px;color:var(--ink)}
.svc .ico{width:48px;height:48px;border-radius:50%;background:radial-gradient(circle at 35% 35%,#e04a5c,var(--red-deep));flex:none;display:flex;align-items:center;justify-content:center}
.svc.active{background:linear-gradient(90deg,var(--red) 0%,var(--red) 45%,var(--teal) 100%);color:var(--white);display:block;padding:12px 18px}
.svc.active b{display:block;font-size:16px;margin-bottom:6px}
.svc.active span{display:block;font-size:11.5px;font-weight:500;line-height:19px}

/* transform band */
.band{position:absolute;left:0;top:1819px;width:1200px;height:458px;background:linear-gradient(90deg,#0f9ea6 0%,var(--teal) 60%,#0b8b92 100%);overflow:hidden}
.band h2{position:absolute;left:617px;top:92px;font-size:33px;line-height:49px;color:var(--white);font-family:"Poppins",sans-serif;font-weight:800;text-transform:uppercase}
.band p{position:absolute;left:617px;top:256px;width:500px;font-size:18px;line-height:33px;color:var(--white)}

/* logos */
.client{position:absolute;top:2469px;width:183px;height:94px;border-radius:12px;background:var(--white);box-shadow:0 4px 16px rgba(0,0,0,.1);display:flex;align-items:center;justify-content:center;gap:8px;font-weight:700;font-size:17px;color:#2b3a55}
.client i{width:14px;height:14px;border-radius:50%;background:var(--teal);display:block}

/* teams */
.teams{position:absolute;left:0;top:2787px;width:1200px;height:558px;background:var(--pale)}
.tab{position:absolute;left:110px;width:321px;height:50px;border-radius:25px;background:var(--white);box-shadow:0 3px 12px rgba(0,0,0,.06);display:flex;align-items:center;gap:18px;padding-left:4px;font-weight:700;font-size:16px;color:var(--teal)}
.tab .dot{width:44px;height:44px;border-radius:50%;background:var(--teal);flex:none;display:flex;align-items:center;justify-content:center}
.tab.active{background:var(--teal);color:var(--white)}
.tab.active .dot{background:var(--red)}
.team-copy h3{position:absolute;left:798px;top:220px;font-family:"Poppins",sans-serif;font-weight:700;font-size:20px;line-height:30px;color:var(--teal);text-transform:uppercase}
.team-copy p{position:absolute;left:798px;top:284px;width:300px;font-size:14.5px;line-height:28px;color:var(--grey)}

.feature h2{position:absolute;font-family:"Poppins",sans-serif;font-weight:700;font-size:32px;line-height:44px;text-transform:uppercase;text-align:center}
.feature p{position:absolute;font-size:17px;line-height:30px;color:var(--grey);text-align:center}

/* cta band */
.cta{position:absolute;left:0;top:4190px;width:1200px;height:243px;background:linear-gradient(90deg,var(--red-deep),var(--red) 50%,var(--red-deep))}
.cta h2{position:absolute;top:52px;font-size:32px;color:var(--white)}
.cta p{position:absolute;top:102px;font-size:17px;font-weight:700;color:var(--white)}

/* footer */
.foot-links a{position:absolute;top:4540px;font-size:16px;color:var(--ink);text-decoration:none;font-weight:500}
.social{position:absolute;top:4581px;width:32px;height:32px;border-radius:50%;background:var(--teal)}
.copy{position:absolute;top:4628px;font-size:12px;color:var(--grey)}
</style>
</head>
<body>

<header class="hero">
  <div class="hero-photo" role="img" aria-label="Photo of a smiling woman with curly hair using a tablet in an office, over a dark data-streaked background"></div>
  <svg class="abs" style="left:0;top:0" width="1200" height="600" viewBox="0 0 1200 600">
    <path d="M0 390 C 250 600, 700 620, 1200 400 L1200 600 L0 600 Z" fill="#ffffff"/>
    <path d="M0 380 C 120 520, 340 600, 560 592 C 820 584, 1020 500, 1200 395 C 1020 480, 800 545, 560 560 C 330 572, 140 500, 0 380 Z" fill="#c8102e"/>
  </svg>
  <div class="abs logo-word" style="left:109px;top:22px;color:#fff">Lumo.app</div>
  <nav class="nav">
    <a class="active" style="left:0">Platform</a>
    <a style="left:100px">Solutions</a>
    <a style="left:204px">Resources</a>
    <a style="left:317px">About Us</a>
    <a style="left:421px">Pricing Plans</a>
  </nav>
  <a class="btn btn-teal" style="left:934px;top:29px;width:152px;height:40px">Book A Demo</a>
  <h1 class="h-display"><span class="l1">Connect</span><span class="l2">The Unconnected</span></h1>
  <p>You know you have a problem.&nbsp; We know why you have a problem.</p>
  <a class="btn btn-teal" style="left:112px;top:366px;width:214px;height:40px">Let's Solve It Together</a>
</header>

<section class="solve">
  <h2 class="sec-title center" style="top:642px">Let's Solve It Together</h2>
  <p class="lead center" style="top:694px;left:190px;width:820px">You're not here by accident. You're also not alone. Many large, complex businesses are facing the same communication challenges... <a>More</a></p>
  <p class="lead-strong center" style="top:774px;left:230px;width:740px">Lumo enables you to bridge the communication gap and develop a more informed, aligned and inspired workplace.</p>
  <a class="btn btn-teal" style="left:429px;top:865px;width:163px;height:40px">Book A Demo</a>
  <a class="btn btn-red" style="left:606px;top:865px;width:165px;height:40px">Watch Video</a>
  <div class="photo" style="left:127px;top:950px;width:302px;height:346px;background:linear-gradient(160deg,#9fb6c8,#6e5a4c 60%,#3c3a40)" role="img" aria-label="Photo of an excited audience raising paper sheets at a workshop"></div>
  <div class="photo" style="left:449px;top:950px;width:302px;height:346px;background:linear-gradient(180deg,#dfe2e4,#8a8d7a 55%,#c9cbc8)" role="img" aria-label="Photo of a team in hi-vis workwear gathered around a meeting table"></div>
  <div class="photo" style="left:771px;top:950px;width:302px;height:346px;background:linear-gradient(180deg,#9aa1a6,#5f666c 50%,#b2b5b4)" role="img" aria-label="Photo of a warehouse aisle stacked with steel pipes"></div>
</section>

<section class="services">
  <h2 class="sec-title center" style="top:1358px">Services We Provide</h2>
  <p class="lead center" style="top:1406px;left:230px;width:740px">Comms teams can easily create and deliver content to all kinds of screens in a vibrant, compelling and memorable format.</p>
  <div class="svc" style="left:107px;top:1495px"><span class="ico"></span>Manage<br>The Culture</div>
  <div class="svc active" style="left:357px;top:1495px"><b>Calm The Noise</b><span>By simplifying the messaging environment, your comms will cut-</span></div>
  <div class="svc" style="left:608px;top:1495px"><span class="ico"></span>Change<br>Behaviour</div>
  <div class="svc" style="left:858px;top:1495px"><span class="ico"></span>Inspire And<br>Excite</div>
  <div class="svc" style="left:107px;top:1609px"><span class="ico"></span>Empower<br>Teams</div>
  <div class="svc" style="left:357px;top:1609px"><span class="ico"></span>Organisational<br>Glue</div>
  <div class="svc" style="left:608px;top:1609px"><span class="ico"></span>Unify<br>The Workplace</div>
  <div class="svc" style="left:858px;top:1609px"><span class="ico"></span>Frontline To<br>Backoffice</div>
  <p class="center abs" style="top:1740px;font-size:18px;font-weight:600;color:var(--red)">Lumo is the one workplace comms platform that reaches &amp; engages everyone, everywhere.</p>
</section>

<section class="band">
  <svg class="abs" style="left:0;top:0" width="600" height="458" viewBox="0 0 600 458">
    <path d="M0 0 H360 C 250 40, 150 120, 150 260 C 150 360, 210 430, 270 458 H0 Z" fill="#c8102e"/>
  </svg>
  <div class="abs" style="left:120px;top:60px;width:440px;height:380px;border-radius:50% 50% 48% 52%;background:linear-gradient(160deg,#e6eef2,#b7c5cc 50%,#6e8590)" role="img" aria-label="Illustration of a woman with glasses working on a laptop, surrounded by floating comms screen tiles"></div>
  <h2>Transform How<br>You Connect With Hard<br>-To-Reach Workers</h2>
  <p>Lumo brings together digital workplace screens, desktops and mobiles to reach all your people – whether they're at home at their desks, on the road or the factory floor.</p>
</section>

<section class="clients">
  <h2 class="sec-title center" style="top:2340px;line-height:49px">Lumo Works For Large, Complex Businesses<br>&amp; It Will Work For You, Too.</h2>
  <div class="client" style="left:101px"><i></i>Gridline</div>
  <div class="client" style="left:304px"><i></i>Aeroreg</div>
  <div class="client" style="left:509px"><i></i>Corelab</div>
  <div class="client" style="left:711px"><i></i>Hartwell Health</div>
  <div class="client" style="left:914px;font-size:15px"><i></i>Storehouse Group</div>
  <p class="lead center" style="top:2594px;left:190px;width:820px;font-size:16.5px">"Insightful, impressive quote from Lumo customer but within quote marks so it looks like recommendation from a real person"&nbsp; <b style="color:var(--red)">Brand</b></p>
  <a class="btn btn-teal" style="left:429px;top:2684px;width:163px;height:40px">Book A Demo</a>
  <a class="btn btn-red" style="left:606px;top:2684px;width:165px;height:40px">Free Trial</a>
</section>

<section class="teams">
  <h2 class="sec-title center" style="top:66px">A Single Platform For All Your Key Teams.</h2>
  <div class="tab active" style="top:144px"><span class="dot"></span>Internal Communications</div>
  <div class="tab" style="top:215px"><span class="dot"></span>Health &amp; Safety</div>
  <div class="tab" style="top:287px"><span class="dot"></span>Learning &amp; Development</div>
  <div class="tab" style="top:358px"><span class="dot"></span>IT &amp; Cybersecurity</div>
  <div class="tab" style="top:428px"><span class="dot"></span>People &amp; Culture</div>
  <div class="photo" style="left:469px;top:145px;width:295px;height:333px;background:linear-gradient(160deg,#2a3442,#5b6470 55%,#1c222a)" role="img" aria-label="Photo of a team gathered around a laptop in a dim office"></div>
  <div class="team-copy">
    <h3>Lumo Works For Internal<br>Comms Teams.</h3>
    <p>Always pushed for time, often stretched for resources and people – Lumo takes a huge load off.</p>
  </div>
  <a class="btn btn-red" style="left:799px;top:371px;width:138px;height:42px">Read More</a>
</section>

<section class="feature">
  <h2 style="left:112px;top:3448px;width:500px">No Need To Play Graphic<br>Designer</h2>
  <p style="left:152px;top:3543px;width:420px">Lumo gives you access to an extensive library of templates, for effortless creation of stunning content.</p>
  <a class="btn btn-red" style="left:289px;top:3651px;width:140px;height:41px">Read More</a>
  <div class="photo" style="left:634px;top:3417px;width:454px;height:317px;background:linear-gradient(150deg,#c9b79c,#8e7a62 50%,#e1ddd5)" role="img" aria-label="Overhead photo of colleagues collaborating around a wooden table with laptops"></div>

  <div class="photo" style="left:139px;top:3783px;width:455px;height:317px;background:linear-gradient(150deg,#dfe6ea,#8b7d78 55%,#c4c9cc)" role="img" aria-label="Photo of a group of young colleagues crowded around a laptop"></div>
  <h2 style="left:624px;top:3815px;width:500px">Bite-Sized Content For<br>Snackable Learning</h2>
  <p style="left:664px;top:3911px;width:420px">Lumo's snackable learning framework delivers messages that are optimally sized and sequenced for uptake and retention.</p>
  <a class="btn btn-red" style="left:800px;top:4016px;width:139px;height:42px">Read More</a>
</section>

<section class="cta">
  <h2 class="h-display center">Transform The Way You Talk To Your Workforce</h2>
  <p class="center">Lumo will enable you to reach &amp; engage everyone, everywhere.</p>
  <a class="btn btn-white" style="left:430px;top:149px;width:160px;height:41px">Book A Demo</a>
  <a class="btn btn-teal" style="left:609px;top:149px;width:161px;height:41px">Find Out More</a>
</section>

<footer>
  <div class="abs logo-word center" style="top:4474px;color:var(--red)">Lumo.app</div>
  <nav class="foot-links">
    <a style="left:254px">Platform</a>
    <a style="left:358px">Solutions</a>
    <a style="left:470px">Resources</a>
    <a style="left:591px">About Us</a>
    <a style="left:702px">Pricing Plans</a>
    <a style="left:841px">Book A Demo</a>
  </nav>
  <span class="social" style="left:543px" aria-label="Social link"></span>
  <span class="social" style="left:583px" aria-label="Social link"></span>
  <span class="social" style="left:623px" aria-label="Social link"></span>
  <p class="copy center">(C) Copyright 2024 | All Rights Reserved</p>
</footer>

</body>
</html>
```